Recruiting ad for Caregivers and Nurses

We need a few amazing, fun, catchy, creative recruiting ads for Caregivers and Nurses to care for homecare patients on the island of Oahu, in Hawaii. We are an in home care company called Brantley Homecare. Our care services are provided 24/7, so we need staff that can work days, nights, weekdays, weekends. We need catchy fun ads to entice caregivers and nurses to call our office to inquire about jobs available. Our patients age range is from babies to seniors. We need caregivers and nurses for basic patient care (bathing, dressing, ambulating, preparing meals, medication reminders, light housekeeping) and complex patients (oxygen, tube feeding, injections, vents, wound care). Here are some bullets to consider including:
*Full-time and Part-time Positions Available (days, nights, weekdays, weekends)
*Sign-On Bonus Programs Offered up to $500
*Refer a Friend Bonus Program
*Holiday Pay
*2 Health Plans to Choose from
*Island-Wide Locations
*All PPE Provided (masks, gloves, etc)
*401K Program
*Tuition Benefits

```html
<!DOCTYPE html>
<html lang="en">
<head>
<meta charset="utf-8">
<title>Brantley Homecare – Caregiver Recruiting Flyer</title>
<link rel="stylesheet" href="https://fonts.googleapis.com/css2?family=Poppins:wght@500;600;700;800;900&display=swap">
<style>
  :root {
    --grey-bg: #dcdde0;
    --teal: #00b3c6;
    --salmon: #f4a085;
    --ink: #1c1c1c;
    --white: #ffffff;
    --scrub-blue: #3a7fd6;
    --bullet-fill: #fde6dc;
  }
  * { margin: 0; padding: 0; box-sizing: border-box; }
  html, body { width: 990px; height: 1200px; overflow: hidden; background: var(--grey-bg); }
  body { font-family: "Poppins", sans-serif; color: var(--ink); }

  .flyer { position: relative; width: 990px; height: 1200px; overflow: hidden; background: var(--grey-bg); }

  .artwork { position: absolute; inset: 0; }

  .headline { position: absolute; left: 0; top: 0; line-height: 1; }
  .headline span { position: absolute; white-space: nowrap; }
  .headline .lead { font-size: 50px; font-weight: 700; color: var(--ink); }
  .headline .lead-1 { left: 146px; top: 64px; }
  .headline .role { left: 96px; top: 118px; font-size: 82px; font-weight: 900; color: var(--salmon); text-shadow: 4px 4px 0 var(--ink); letter-spacing: -1px; }
  .headline .lead-2 { left: 98px; top: 206px; }
  .headline .job { left: 132px; top: 250px; font-size: 140px; font-weight: 900; color: var(--teal); text-shadow: 5px 5px 0 var(--ink); letter-spacing: -4px; }
  .headline .lead-3 { left: 130px; top: 374px; }

  .benefits { position: absolute; left: 103px; top: 568px; list-style: none; font-size: 19.5px; font-weight: 500; line-height: 1.4; }
  .benefits li { position: relative; padding-left: 21px; margin-bottom: 9px; }
  .benefits li::before {
    content: ""; position: absolute; left: 0; top: 8px; width: 13px; height: 13px;
    border: 2px solid var(--salmon); border-radius: 3px; background: var(--bullet-fill);
  }
  .benefits .note { display: block; }

  .contact { position: absolute; left: 100px; top: 998px; }
  .address { position: relative; padding-left: 28px; font-size: 20px; font-weight: 500; line-height: 1.35; }
  .address svg { position: absolute; left: 4px; top: 2px; }
  .phone {
    display: flex; align-items: center; margin-top: 10px; width: 421px; height: 48px;
    background: var(--teal); border-radius: 24px; color: var(--white);
    font-size: 42px; font-weight: 700; letter-spacing: -0.5px;
  }
  .phone-icon {
    width: 52px; height: 52px; border-radius: 50%; background: var(--white);
    border: 4px solid var(--teal); display: flex; align-items: center; justify-content: center; margin-right: 16px; margin-left: -2px;
  }
  .website { margin-top: 10px; font-size: 34px; font-weight: 700; letter-spacing: .4px; }

  .brand-seal {
    position: absolute; left: 576px; top: 908px; width: 330px; height: 330px;
    border-radius: 50%; background: var(--white);
    display: flex; flex-direction: column; align-items: center; justify-content: center; padding-bottom: 40px;
  }
  .brand-square { width: 56px; height: 56px; background: var(--ink); border-radius: 6px; margin-bottom: 18px; }
  .brand-name { font-size: 42px; font-weight: 600; color: var(--ink); text-align: center; line-height: 1.05; }
</style>
</head>
<body>
<div class="flyer">
  <svg class="artwork" width="990" height="1200" viewBox="0 0 990 1200">
    <defs>
      <linearGradient id="nurse-tone" x1="0" y1="0" x2="0" y2="1">
        <stop offset="0" stop-color="#dcdde0"/>
        <stop offset="0.35" stop-color="#8fb3e4"/>
        <stop offset="1" stop-color="#3a7fd6"/>
      </linearGradient>
      <linearGradient id="home-tone" x1="0" y1="0" x2="1" y2="0">
        <stop offset="0" stop-color="#ffffff" stop-opacity="0"/>
        <stop offset="0.3" stop-color="#efe4cf" stop-opacity="0.7"/>
        <stop offset="0.6" stop-color="#a9c3de" stop-opacity="0.85"/>
        <stop offset="1" stop-color="#8fd0dc" stop-opacity="0.9"/>
      </linearGradient>
      <clipPath id="content-panel">
        <path d="M0,616 C120,538 260,500 400,504 C560,510 700,564 800,558 C880,554 940,528 990,488 L990,1200 L0,1200 Z"/>
      </clipPath>
    </defs>

    <rect role="img" aria-label="Photo of a smiling caregiver in blue scrubs with a stethoscope" x="495" y="30" width="475" height="500" rx="40" fill="url(#nurse-tone)"/>

    <path d="M0,596 C110,500 240,445 380,448 C540,452 700,505 800,500 C880,496 940,460 990,412 L990,1200 L0,1200 Z" fill="var(--teal)"/>
    <path d="M0,610 C120,530 260,492 400,496 C560,502 700,555 800,550 C880,546 940,520 990,478 L990,1200 L0,1200 Z" fill="var(--salmon)"/>
    <path d="M0,616 C120,538 260,500 400,504 C560,510 700,564 800,558 C880,554 940,528 990,488 L990,1200 L0,1200 Z" fill="var(--white)"/>

    <g clip-path="url(#content-panel)">
      <rect role="img" aria-label="Faded photo of a caregiver laughing with an older woman on a sofa at home" x="500" y="480" width="490" height="540" fill="url(#home-tone)"/>
    </g>

    <path d="M40,1010 C160,950 320,930 480,955 C600,975 700,1025 800,1020 C880,1015 940,960 990,890 L990,1200 L40,1200 Z" fill="var(--teal)"/>
    <path d="M0,1025 C150,962 320,945 480,970 C600,990 700,1045 800,1040 C880,1035 940,980 990,908 L990,1200 L0,1200 Z" fill="var(--salmon)"/>
  </svg>

  <h1 class="headline">
    <span class="lead lead-1">are you a</span>
    <span class="role">Caregiver?</span>
    <span class="lead lead-2">we have a</span>
    <span class="job">Job</span>
    <span class="lead lead-3">for you!</span>
  </h1>

  <ul class="benefits">
    <li>Full-time and Part-time Positions Available<span class="note">(days, nights, weekdays, weekends)</span></li>
    <li>Sign-On Bonus Programs Offered up to $500</li>
    <li>Refer a Friend Bonus Program</li>
    <li>Holiday Pay</li>
    <li>2 Health Plans to Choose from</li>
    <li>Island-Wide Locations</li>
    <li>All PPE Provided (masks, gloves, etc)</li>
    <li>401K Program</li>
    <li>Tuition Benefits</li>
  </ul>

  <div class="contact">
    <p class="address">
      <svg width="14" height="20" viewBox="0 0 14 20" aria-hidden="true"><circle cx="7" cy="6" r="4.5" fill="none" stroke="var(--ink)" stroke-width="1.6"/><path d="M7,10.5 V17 M2,18.5 H12" stroke="var(--ink)" stroke-width="1.6"/></svg>
      1450 Makana Ave. Suite 310<br>Honolulu HI, 96815
    </p>
    <p class="phone">
      <span class="phone-icon"><svg width="26" height="26" viewBox="0 0 24 24" aria-hidden="true"><path d="M6.6 10.8a15.1 15.1 0 0 0 6.6 6.6l2.2-2.2c.3-.3.7-.4 1-.2 1.1.4 2.3.6 3.6.6.6 0 1 .4 1 1V20c0 .6-.4 1-1 1A17 17 0 0 1 3 4c0-.6.4-1 1-1h3.5c.6 0 1 .4 1 1 0 1.3.2 2.5.6 3.6.1.3 0 .7-.2 1z" fill="var(--teal)"/></svg></span>
      808-555-0172
    </p>
    <p class="website">www.brantleycare.com</p>
  </div>

  <div class="brand-seal">
    <div class="brand-square"></div>
    <p class="brand-name">Brantley<br>Homecare</p>
  </div>
</div>
</body>
</html>
```